Havenmark Electrical Business Card

create a simple but clear business card and letterhead - needs to be professional not too fancy and direct.

Target Market(s)

Home builders

Contact Information for Business Card

Information needed
Havenmark Electrical Contracting
EC. No. 418237
Derek Hollowell
Mobile 0437215609
derek@havenmarkelectrical.com.au

Requirements
Must have
• logo
• Havenmark Electrical Contracting - H.E.C.
• EC. No. 418237
• Derek Hollowell
• Mobile 0437215609
• derek@havenmarkelectrical.com.au
Nice to have
• black with white printing simple but clear
Should not have
• too much information
• no fancy writing

```html
<!DOCTYPE html>
<html lang="en">
<head>
<meta charset="utf-8">
<title>Havenmark Electrical Contracting – Business Card</title>
<link rel="stylesheet" href="https://fonts.googleapis.com/css2?family=Tinos:wght@400;700&display=swap">
<style>
  :root {
    --backdrop: #2b2b2b;
    --ink: #000000;
    --paper: #ffffff;
    --faint-mark: #0d0d0d;
  }
  * { margin: 0; padding: 0; box-sizing: border-box; }
  html, body {
    width: 1189px; height: 1200px; overflow: hidden;
    background: var(--backdrop);
    font-family: "Tinos", "Times New Roman", serif;
  }
  .card {
    position: absolute;
    left: 171px;
    width: 833px;
    height: 486px;
    overflow: hidden;
    box-shadow: 0 6px 18px rgba(0,0,0,.45);
  }
  .card--front { top: 69px; background: var(--ink); }
  .card--back { top: 628px; background: var(--paper); }

  .faint-mark {
    position: absolute;
    left: 106px; top: -4px;
    width: 490px; height: 490px;
    border-radius: 50%;
    background: var(--faint-mark);
  }

  .brand { position: absolute; display: flex; align-items: center; gap: 20px; }
  .brand__dot { width: 100px; height: 100px; border-radius: 50%; flex: none; }
  .brand__name { font-weight: 700; line-height: 1.05; }
  .brand__name .line-main { display: block; font-size: 44px; letter-spacing: 1px; }
  .brand__name .line-sub { display: block; font-size: 27px; }

  .card--front .brand { left: 143px; top: 163px; color: var(--paper); }
  .card--front .brand__dot { background: var(--paper); }
  .card--back .brand { left: 42px; top: 57px; color: var(--ink); }
  .card--back .brand__dot { background: var(--ink); }

  .back-sweep { position: absolute; inset: 0; width: 100%; height: 100%; }

  .contact { position: absolute; color: var(--paper); font-weight: 700; text-align: right; }
  .contact__name { position: absolute; right: 10px; top: 276px; font-size: 27px; white-space: nowrap; }
  .contact__line {
    position: absolute; right: 10px; font-size: 20px; white-space: nowrap;
    display: flex; align-items: center; gap: 10px;
  }
  .contact__line--phone { top: 367px; }
  .contact__line--email { top: 396px; }
  .contact__line--licence { top: 428px; right: 10px; }
  .icon { width: 16px; height: 19px; flex: none; }
</style>
</head>
<body>
  <section class="card card--front" aria-label="Card front">
    <div class="faint-mark"></div>
    <div class="brand">
      <span class="brand__dot"></span>
      <span class="brand__name">
        <span class="line-main">HAVENMARK</span>
        <span class="line-sub">Electrical Contracting</span>
      </span>
    </div>
  </section>

  <section class="card card--back" aria-label="Card back">
    <svg class="back-sweep" viewBox="0 0 1020 595" preserveAspectRatio="none" aria-hidden="true">
      <path d="M890 0 L1020 0 L1020 595 L30 595 C310 520 780 330 890 0 Z" fill="var(--ink)"/>
      <path d="M858 82 C770 380 330 545 28 592 C350 558 800 360 858 82 Z" fill="var(--paper)"/>
    </svg>
    <div class="brand">
      <span class="brand__dot"></span>
      <span class="brand__name">
        <span class="line-main">HAVENMARK</span>
        <span class="line-sub">Electrical Contracting</span>
      </span>
    </div>
    <div class="contact">
    </div>
    <div class="contact" style="inset:0">
      <p class="contact__name">Derek Hollowell</p>
      <p class="contact__line contact__line--phone">0437215609
        <svg class="icon" viewBox="0 0 16 19" aria-hidden="true">
          <rect width="16" height="19" fill="var(--paper)"/>
          <path d="M5 4 L7 4 L8 7 L6.5 8 C7 10 8 11.5 9.5 12.5 L10.5 11 L13 12 L13 14 C9 15 4 10 5 4 Z" fill="var(--ink)"/>
        </svg>
      </p>
      <p class="contact__line contact__line--email">derek@havenmarkelectrical.com.au
        <svg class="icon" viewBox="0 0 16 19" aria-hidden="true">
          <rect width="16" height="19" fill="var(--paper)"/>
          <rect x="2.5" y="5.5" width="11" height="8" fill="none" stroke="var(--ink)" stroke-width="1.2"/>
          <path d="M2.5 5.5 L8 10 L13.5 5.5 M2.5 13.5 L6.5 9 M13.5 13.5 L9.5 9" fill="none" stroke="var(--ink)" stroke-width="1.2"/>
        </svg>
      </p>
      <p class="contact__line contact__line--licence">EC. No. 418237</p>
    </div>
  </section>
</body>
</html>
```